Harbor Line IT Service, Technology & Security Co.

need a new business card design for our Technology & Security Company. We are a Computer Networking Company, Security Camera Installers, Phone Systems.

Target Market(s)

Construction, Medical, Law Offices, Accounting, Retail etc.

Industry/Entity Type

Information Technology

Logo is attached, colors are Blue, Red, Black. Blue for Technology & Red is for Security Cameras, Access Control, Alarm Systems

Colors
fbed22
ec1f27
0555a3
ffffff

Requirements
Must have
• Pictures or Icons for
• For Technology:
• Computer, Network, Phone System, Copier, TV, Cabling
• For Security:
• Video Surveillance, Access Control, Intercom, Fire Alarm, Burglar Alarm, Time Clock

```html
<!DOCTYPE html>
<html lang="en">
<head>
<meta charset="utf-8">
<title>Harbor Line IT Service – Business Card</title>
<link href="https://fonts.googleapis.com/css2?family=Montserrat:wght@800&family=Jost:wght@400;500&display=swap" rel="stylesheet">
<style>
  :root {
    --backdrop: #2b2b2b;
    --card-dark: #1c1c1c;
    --card-light: #ffffff;
    --tech-blue: #0555a3;
    --security-red: #ec1f27;
    --ink: #1a1a1a;
    --muted: #6d6d6d;
    --paper-text: #f2f2f2;
  }
  * { box-sizing: border-box; margin: 0; padding: 0; }
  html, body { width: 1200px; height: 930px; overflow: hidden; }
  body {
    background: var(--backdrop);
    display: flex;
    flex-direction: column;
    align-items: center;
    justify-content: center;
    gap: 60px;
    font-family: "Jost", sans-serif;
  }
  .card {
    width: 600px;
    height: 343px;
    position: relative;
    overflow: hidden;
    box-shadow: 0 14px 30px rgba(0,0,0,.45);
  }

  /* Back side */
  .card-back {
    background: var(--card-dark);
    color: var(--paper-text);
    display: flex;
    flex-direction: column;
    align-items: center;
    padding-top: 58px;
  }
  .brand { display: flex; align-items: center; gap: 10px; }
  .brand-dot { width: 16px; height: 16px; border-radius: 50%; background: var(--security-red); }
  .brand-name {
    font-family: "Montserrat", sans-serif;
    font-weight: 800;
    font-size: 27px;
    letter-spacing: -0.5px;
  }
  .card-back .brand-name { color: #ffffff; }
  .service-group { display: flex; flex-direction: column; align-items: center; margin-top: 30px; }
  .service-group + .service-group { margin-top: 22px; }
  .icon-row { display: flex; gap: 10px; }
  .icon {
    width: 26px; height: 26px; border-radius: 50%;
    display: flex; align-items: center; justify-content: center;
  }
  .icon svg { width: 15px; height: 15px; stroke: #fff; fill: none; stroke-width: 1.6; stroke-linecap: round; stroke-linejoin: round; }
  .icon-tech { background: var(--tech-blue); }
  .icon-security { background: var(--security-red); }
  .service-list { font-size: 14px; letter-spacing: .4px; text-align: center; line-height: 1.35; margin-top: 8px; }

  /* Front side */
  .card-front { background: var(--card-light); color: var(--ink); }
  .card-front .brand { position: absolute; left: 44px; top: 58px; }
  .card-front .brand-name { color: var(--ink); font-size: 24px; }
  .accent-art {
    position: absolute; right: 0; top: 0; width: 250px; height: 343px;
    background: radial-gradient(ellipse at 55% 45%, rgba(236,31,39,.22), rgba(5,85,163,.14) 45%, rgba(255,255,255,0) 72%);
  }
  .person { position: absolute; left: 44px; top: 140px; }
  .person-name { font-family: "Montserrat", sans-serif; font-weight: 800; color: var(--tech-blue); font-size: 20px; letter-spacing: .3px; }
  .person-role { color: var(--muted); font-size: 15px; margin-top: 2px; }
  .contact-list { position: absolute; left: 44px; bottom: 36px; list-style: none; color: var(--muted); font-size: 14.5px; }
  .contact-list li { display: flex; align-items: center; gap: 10px; line-height: 1.6; }
  .contact-list svg { width: 13px; height: 13px; fill: var(--tech-blue); }
  .address { position: absolute; left: 330px; bottom: 70px; color: var(--muted); font-size: 14.5px; line-height: 1.4; }
</style>
</head>
<body>

<section class="card card-back" aria-label="Business card back">
  <div class="brand">
    <span class="brand-dot"></span>
    <span class="brand-name">HARBOR LINE IT SERVICE</span>
  </div>

  <div class="service-group">
    <div class="icon-row">
      <span class="icon icon-tech"><svg viewBox="0 0 16 16"><rect x="2" y="3" width="12" height="8" rx="1"/><path d="M6 14h4M8 11v3"/></svg></span>
      <span class="icon icon-tech"><svg viewBox="0 0 16 16"><circle cx="4" cy="8" r="2"/><circle cx="12" cy="4" r="2"/><circle cx="12" cy="12" r="2"/><path d="M6 7l4-2M6 9l4 2"/></svg></span>
      <span class="icon icon-tech"><svg viewBox="0 0 16 16"><rect x="5" y="2" width="6" height="12" rx="1"/><path d="M7.5 12h1"/></svg></span>
      <span class="icon icon-tech"><svg viewBox="0 0 16 16"><rect x="2" y="6" width="12" height="6" rx="1"/><path d="M4 6V3h8v3M5 12v2h6v-2"/></svg></span>
      <span class="icon icon-tech"><svg viewBox="0 0 16 16"><rect x="2" y="3" width="12" height="8" rx="1"/><path d="M5 13h6"/></svg></span>
      <span class="icon icon-tech"><svg viewBox="0 0 16 16"><path d="M5 2v5a2 2 0 0 0 4 0V2M7 9v5M11 6v8"/></svg></span>
    </div>
    <p class="service-list">Computer, Network, Phone System, Copier, TV, Cabling</p>
  </div>

  <div class="service-group">
    <div class="icon-row">
      <span class="icon icon-security"><svg viewBox="0 0 16 16"><rect x="2" y="5" width="9" height="5" rx="1"/><path d="M11 7l3-2v5l-3-2M5 10v3"/></svg></span>
      <span class="icon icon-security"><svg viewBox="0 0 16 16"><rect x="4" y="2" width="8" height="12" rx="1"/><path d="M6 5h4M6 8h4M6 11h2"/></svg></span>
      <span class="icon icon-security"><svg viewBox="0 0 16 16"><rect x="3" y="3" width="10" height="10" rx="1"/><circle cx="8" cy="7" r="1.5"/><path d="M6 11h4"/></svg></span>
      <span class="icon icon-security"><svg viewBox="0 0 16 16"><path d="M4 12a4 4 0 0 1 8 0M3 14h10M8 2v2M3 5l1.5 1M13 5l-1.5 1"/></svg></span>
      <span class="icon icon-security"><svg viewBox="0 0 16 16"><circle cx="8" cy="8" r="1.5"/><path d="M5 5a4 4 0 0 0 0 6M11 5a4 4 0 0 1 0 6M3 3a7 7 0 0 0 0 10M13 3a7 7 0 0 1 0 10"/></svg></span>
      <span class="icon icon-security"><svg viewBox="0 0 16 16"><circle cx="8" cy="8" r="6"/><path d="M8 4.5V8l2.5 1.5"/></svg></span>
    </div>
    <p class="service-list">Video Surveillance, Access Control,<br>Intercom, Fire Alarm, Burglar Alarm, Time Clock</p>
  </div>
</section>

<section class="card card-front" aria-label="Business card front">
  <div class="brand">
    <span class="brand-dot"></span>
    <span class="brand-name">HARBOR LINE IT SERVICE</span>
  </div>

  <div class="accent-art" role="img" aria-label="Large brand emblem in red and blue rising upward"></div>

  <div class="person">
    <p class="person-name">DANIEL REYES</p>
    <p class="person-role">Founder</p>
  </div>

  <ul class="contact-list">
    <li><svg viewBox="0 0 16 16"><rect x="4" y="1" width="8" height="14" rx="1.5"/></svg>800-555-0142</li>
    <li><svg viewBox="0 0 16 16"><path d="M1 3h14v10H1z"/></svg>dreyes@harborlineit.com</li>
    <li><svg viewBox="0 0 16 16"><circle cx="8" cy="8" r="7"/></svg>harborlineit.com</li>
  </ul>

  <p class="address">4410 Canal Street,<br>Suite C7 Phoenix 85016</p>
</section>

</body>
</html>
```